DL Flyer for vehicle buying/selling service and advice business

New business to help people sell their current vehicle then select and buy and maintain their next car. (New or used).
We'll prepare and sell your car for you and get $,000s more than a trade in.
Offer advice as to the best car currently on the market based on our customer's needs.
With country wide sourcing network of cars across all manufacturers we have great buying power to ensure the very best possible price.
Personal service, including preparation of car for sale, pickup of old and drop-off of new vehicles, organise RWC and any required repairs.
We are NOT a car dealer so we WILL not try to sell you the vehicles we own.
Totally impartial, professional and friendly service making the purchase of your next car a great experience.
Updates

Flyer wording===========“Don’t sell your car or buy your next car without speaking to us”We guarantee to get you a better price for your current car and to find a cheaper purchase price for your next car.With a country wide sourcing network of cars “new and used” across all manufacturers we have sensational buying power to ensure the very best possible price.We can source the right car on any budget, from $2,000 to $200,000We are NOT a car dealer so we WILL not try to sell you the vehicles we own.By not being affiliated with any individual car manufacturer or dealer we can offer absolute impartiality.We’ll sit with you to discuss the best car for your needs and even bring the car to you for a test drive without the pressure of a salesperson nearby.Our services include:• Selling your current car: - Obtaining a roadworthy certificate - Organising any repairs needed - Detailing your car (wash, vacuum, polish) - Advertising of your car - Dealing with potential buyers - Negotiating the best price on your behalf• Assisting with the selection of your next car• Organising test drives• Purchasing the car of your choice - Sourcing the very best price• Ongoing management of their vehicle (service, clean, repair)Possible inclusions in the flyer might be:Advantages of upgrading to a new vehicle include:o reliability, o safety,o fuel efficiencyo comfort.Space for a couple of short testimonials Background images of all of the major car manufacturers Added Friday, July 29, 2016

Target Market(s)

Local community.
Initially will drop DL flyers in local post boxes

Industry/Entity Type

Business

Requirements
Must have
• Flyer wording:
• ===========
• “Don’t sell your car or buy your next car without speaking to us”
• ---------------------------------------------------------------------------------
• We guarantee to get you a better price for your current car and to find a cheaper purchase price for your next car.
• With a country wide sourcing network of cars “new and used” across all manufacturers we have sensational buying power to ensure the very best possible price.
• We can source the right car on any budget, from $2,000 to $200,000
• We are NOT a car dealer so we WILL not try to sell you the vehicles we own.
• By not being affiliated with any individual car manufacturer or dealer we can offer absolute impartiality.
• We’ll sit with you to discuss the best car for your needs and even bring the car to you for a test drive without the pressure of a salesperson nearby.
• Our services include:
• • Selling your current car:
• o Obtaining a roadworthy certificate
• o Organising any repairs needed
• o Detailing your car (wash, vacuum, polish)
• o Advertising of your car
• o Dealing with potential buyers
• o Negotiating the best price on your behalf
• • Assisting with the selection of your next car
• • Organising test drives
• • Purchasing the car of your choice
• o Sourcing the very best price
• • Ongoing management of your vehicle (service, clean, repair)
• Call Gerald on: 0427 315064
Nice to have
• Possible inclusions on the flyer might be:
• List of advantages of upgrading to a new vehicle:
• o reliability,
• o safety,
• o fuel efficiency
• o comfort
• Space for a couple of short testimonials
• Background images of all of the major car manufacturers

```html
<!DOCTYPE html>
<html lang="en">
<head>
<meta charset="utf-8">
<title>MotorWise4U DL Flyer</title>
<link rel="stylesheet" href="https://fonts.googleapis.com/css2?family=Bebas+Neue&family=Oswald:wght@400;500&family=Open+Sans:ital,wght@0,400;0,600;0,700;1,400&family=Roboto+Condensed:wght@400&display=swap">
<style>
:root{
  --orange:#ff5a00;
  --orange-light:#ff8a1e;
  --charcoal:#2f2f2f;
  --ink:#1c1c1c;
  --paper:#f1f1f1;
  --paper-shade:#dcdcdc;
  --backdrop:#f4f4f4;
  --white:#ffffff;
}
*{box-sizing:border-box;margin:0;padding:0}
html,body{width:1200px;height:1200px;overflow:hidden;background:var(--backdrop)}
.sheet{position:relative;width:1200px;height:1200px}
.panel{position:absolute;top:111px;width:490px;height:979px;overflow:hidden;
  background:linear-gradient(180deg,var(--white) 0%,var(--paper) 50%,var(--paper-shade) 100%)}
.panel--front{left:84px}
.panel--back{left:618px}
.shapes{position:absolute;left:0;top:0}
.brand{position:absolute;left:0;width:100%;text-align:center;font-family:"Bebas Neue",sans-serif;
  color:var(--charcoal);letter-spacing:6px;line-height:1}
.panel--front .brand{top:428px;font-size:50px}
.panel--back .brand{top:52px;font-size:54px}
.offer-box{position:absolute;left:33px;top:506px;width:424px;height:174px;border-radius:0 0 16px 16px;
  background:linear-gradient(90deg,var(--orange) 0%,var(--orange-light) 100%);
  padding:28px 24px 0 26px;font-family:"Bebas Neue",sans-serif;color:var(--charcoal);line-height:1}
.offer-box .big{font-size:42px;letter-spacing:.3px}
.offer-box .small{font-size:35px;margin-top:4px}
.guarantee{position:absolute;left:33px;top:724px;width:424px;text-align:center}
.guarantee h2{font-family:"Bebas Neue",sans-serif;font-weight:400;color:var(--orange);font-size:31px;line-height:1}
.guarantee p{font-family:"Open Sans",sans-serif;font-size:15.5px;line-height:21px;color:var(--ink);
  text-align:justify;text-align-last:center;margin-top:6px}
.footer-band{position:absolute;left:0;top:923px;width:100%;height:56px;background:var(--charcoal);
  border-top:5px solid var(--orange)}
.call-pill{position:absolute;left:36px;top:891px;width:418px;height:55px;border-radius:28px;background:var(--orange);
  color:var(--white);font-family:"Bebas Neue",sans-serif;font-size:36px;line-height:57px;text-align:center;letter-spacing:.3px}
.headline{position:absolute;left:20px;top:128px;width:450px;text-align:center;font-family:"Oswald",sans-serif;
  font-weight:500;color:var(--white);font-size:33px;line-height:38px;letter-spacing:-.3px}
.intro{position:absolute;left:32px;top:226px;width:426px;font-family:"Open Sans",sans-serif;font-weight:600;
  font-size:15.8px;line-height:22px;color:var(--ink);text-align:justify;text-align-last:center}
.section-title{position:absolute;left:0;width:100%;text-align:center;font-family:"Bebas Neue",sans-serif;
  color:var(--orange);font-size:36px;line-height:1}
.section-title span{border-bottom:2px solid var(--orange)}
.title-services{top:524px}
.title-testimonial{top:714px}
.services{position:absolute;top:574px;list-style:none;font-family:"Roboto Condensed",sans-serif;
  font-size:12.4px;line-height:18px;color:var(--ink)}
.services--left{left:32px;width:215px}
.services--right{left:254px;width:225px}
.services li{position:relative;padding-left:16px}
.services li::before{content:"";position:absolute;left:0;top:5px;width:8px;height:8px;border-radius:50%;background:var(--orange)}
.services li.cont{padding-left:16px}
.services li.cont::before{display:none}
.quote{position:absolute;left:32px;top:765px;width:430px;font-family:"Open Sans",sans-serif;font-style:italic;
  font-size:14.5px;line-height:19.5px;color:var(--ink);text-align:justify;text-align-last:center}
.quote .mark{color:var(--orange);font-weight:700;font-size:18px}
</style>
</head>
<body>
<div class="sheet">

  <section class="panel panel--front">
    <svg class="shapes" width="490" height="430" viewBox="0 0 490 430" aria-hidden="false">
      <polygon role="img" aria-label="Photo of two smiling women beside a car, one holding up car keys"
        points="0,0 490,0 490,260 0,355" fill="#8a7f78"/>
      <polygon points="0,355 490,250 490,275 0,410" fill="#ff5a00"/>
      <polygon points="120,385 490,285 490,298 200,380" fill="#ffffff"/>
    </svg>
    <div class="brand">MOTORWISE4U</div>
    <div class="offer-box">
      <div class="big">Before you sell your car<br>or buy a new car call us..</div>
      <div class="small">We will get you a better price</div>
    </div>
    <div class="guarantee">
      <h2>We guarantee to get you a better price</h2>
      <p>for your current car and to find a cheaper purchase price for your next car. With a country wide sourcing network of cars “new and used” across all manufacturers we have sensational buying power to ensure the very best possible price.</p>
    </div>
    <div class="footer-band"></div>
    <div class="call-pill">Call Gerald on: 0427 315064</div>
  </section>

  <section class="panel panel--back">
    <svg class="shapes" width="490" height="560" viewBox="0 0 490 560">
      <polygon points="0,0 490,0 490,498 0,383" fill="#ff6a0a"/>
      <polygon points="0,383 490,498 490,549 0,434" fill="#2f2f2f"/>
      <polygon points="0,434 490,549 490,560 0,445" fill="#ffffff"/>
    </svg>
    <div class="brand">MOTORWISE4U</div>
    <div class="headline">We can source the right car on any<br>budget, from $2,000 to $200,000</div>
    <p class="intro">We are NOT a car dealer so we WILL not try to sell you the vehicles we own. By not being affiliated with any individual car manufacturer or dealer we can offer absolute impartiality. We’ll sit with you to discuss the best car for your needs and even bring the car to you for a test drive without the pressure of a salesperson nearby.</p>
    <h2 class="section-title title-services"><span>Our Services</span></h2>
    <ul class="services services--left">
      <li>Obtaining a roadworthy certificate</li>
      <li>Organising any repairs needed</li>
      <li>Detailing your car (wash, vacuum, polish)</li>
      <li>Advertising of your car</li>
      <li>Dealing with potential buyers</li>
      <li>Negotiating the best price on your behalf</li>
    </ul>
    <ul class="services services--right">
      <li>Assisting with the selection of your next car</li>
      <li>Organising test drives</li>
      <li>Purchasing the car of your choice</li>
      <li>Sourcing the very best price</li>
      <li>Ongoing management of your vehicle</li>
      <li class="cont">(service, clean, repair)</li>
    </ul>
    <h2 class="section-title title-testimonial"><span>Testimonial</span></h2>
    <p class="quote"><span class="mark">“</span> Lorem ipsum dolor sit amet, consectetuer adipiscing elit, sed diam nonummy nibh euismod tincidunt ut laoreet dolore magna aliquam erat volutpat. Lorem ipsum dolor sit amet, consectetuer adipiscing elit, sed diam nonummy nibh euismod tincidunt ut laoreet dolore magna aliquam erat volutpat. <span class="mark">”</span></p>
    <div class="footer-band"></div>
    <div class="call-pill">Call Gerald on: 0427 315064</div>
  </section>

</div>
</body>
</html>
```